Crossword App Main Page Design

For a crossword application we need a main page. I am enclosing the current temporary design. There will be 5 buttons. We want a simple but attractive design. Vector designs are preferred. Thank you very much for your interest.
The name of the application is Polyglyph Gridword Riddle and the motto is "gridplay rebuilt." So please use this name on the screen.
Thwe designs I have received so far almost the same with one I have attached. Only the button colors and background image are different. Please try different placement and buttons.
Thanks

```html
<!DOCTYPE html>
<html lang="en">
<head>
<meta charset="utf-8">
<title>Polyglyph Gridword Riddle – Main Menu</title>
<link rel="stylesheet" href="https://fonts.googleapis.com/css2?family=Lilita+One&family=Arimo:wght@700&display=swap">
<style>
  :root {
    --stage-bg: #2a2a2c;
    --screen-warm-light: #ffe58a;
    --screen-warm-mid: #ffc43d;
    --screen-warm-deep: #f59a1c;
    --screen-streak: #e8431c;
    --title-blue: #1f5fc4;
    --motto-ink: #7a3a06;
    --button-top: #5cc2ff;
    --button-mid: #1a7fe0;
    --button-bottom: #0a3f92;
    --button-edge: #072a63;
    --button-label: #ffe21a;
  }

  * { box-sizing: border-box; margin: 0; padding: 0; }

  html, body {
    width: 1200px;
    height: 1188px;
    overflow: hidden;
    background: var(--stage-bg);
  }

  .canvas {
    position: relative;
    width: 1200px;
    height: 1188px;
  }

  .app-screen {
    position: absolute;
    left: 270px;
    top: 155px;
    width: 660px;
    height: 878px;
    overflow: hidden;
    background: var(--screen-warm-mid);
  }

  .screen-artwork {
    position: absolute;
    inset: 0;
    background:
      linear-gradient(160deg, var(--screen-streak) 0%, var(--screen-warm-deep) 16%, transparent 30%),
      radial-gradient(ellipse at 55% 60%, var(--screen-warm-light) 0%, var(--screen-warm-mid) 55%, var(--screen-warm-deep) 100%);
  }

  .app-header {
    position: absolute;
    left: 0;
    right: 0;
    top: 140px;
    text-align: center;
  }

  .app-title {
    font-family: "Lilita One", sans-serif;
    font-weight: 400;
    font-size: 50px;
    line-height: 1;
    color: var(--title-blue);
    letter-spacing: 0.5px;
  }

  .app-motto {
    margin-top: 16px;
    font-family: "Arimo", sans-serif;
    font-weight: 700;
    font-size: 26px;
    line-height: 1;
    color: var(--motto-ink);
  }

  .menu-button {
    display: flex;
    align-items: center;
    justify-content: center;
    border: 2px solid var(--button-edge);
    background: linear-gradient(180deg, var(--button-top) 0%, var(--button-mid) 48%, var(--button-bottom) 100%);
    font-family: "Arimo", sans-serif;
    font-weight: 700;
    color: var(--button-label);
    text-align: center;
  }

  .play-button {
    position: absolute;
    left: 150px;
    top: 320px;
    width: 360px;
    height: 92px;
    border-radius: 46px;
    font-size: 42px;
    letter-spacing: 2px;
  }

  .menu-grid {
    position: absolute;
    left: 65px;
    top: 462px;
    width: 530px;
    display: grid;
    grid-template-columns: 250px 250px;
    grid-auto-rows: 120px;
    gap: 30px;
    list-style: none;
  }

  .menu-grid .menu-button {
    border-radius: 22px;
    font-size: 28px;
  }
</style>
</head>
<body>
  <main class="canvas">
    <section class="app-screen" aria-label="Main menu screen">
      <div class="screen-artwork" role="img" aria-label="Warm orange and yellow background artwork of a crossword grid with scattered letters and red light streaks across the top"></div>

      <header class="app-header">
        <h1 class="app-title">Polyglyph Gridword Riddle</h1>
        <p class="app-motto">gridplay rebuilt.</p>
      </header>

      <div class="menu-button play-button">PLAY</div>

      <ul class="menu-grid">
        <li class="menu-button">My Puzzles</li>
        <li class="menu-button">Buy Puzzle</li>
        <li class="menu-button">About</li>
        <li class="menu-button">Setting</li>
      </ul>
    </section>
  </main>
</body>
</html>
```